UI Improvement for FlorQuay app

We are looking for a talented UI/UX designer to REFINE and enhance the visual design of our mobile application, FlorQuay. The app is fully functional, but we need a designer to improve its aesthetics by specifying design elements such as fonts, colors, spacing, and component styles.
Your task will be to analyze the CURRENT UI and provide detailed design specifications that will make the app more visually appealing, modern, and user-friendly.
TODO:
Review the existing FlorQuay app design (see attachments) and identify areas for visual improvement.
Provide a detailed UI style guide, including:
Typography (font choices, sizes, and weights)
Color palette (primary, secondary, and accent colors)
Component styling (buttons, forms, icons, and interactive elements)
Spacing and layout guidelines (margins, paddings, and alignment)
Ensure the design remains clean, modern, and professional while maintaining usability and accessibility.
Provide design mockups or visual examples (if possible) to illustrate the proposed changes.
Deliverables:
A UI Style Guide (PDF or Figma file) with specifications on fonts, colors, spacing, and UI components.
Optionally, before/after mockups or examples demonstrating the improvements.
Ideal Designer:
Strong experience in mobile UI/UX design.
Understanding of modern design trends and best practices.
Ability to communicate design choices clearly for easy developer implementation.
I have attached 7 images showcasing the main UI screens used in the FlorQuay app. These screens need visual enhancements to improve their overall look and user experience.
The images represent the current design in three key modes:
LIST Mode – Displays data in a structured list format.
READ Mode – Shows detailed information when a user selects an item.
ADD/EDIT Mode – Allows users to input or modify information.
Additionally, there is a ‘MORE’ page, which serves as a menu listing other features of the application.
Task Objective:
Please refine and improve these UIs to create a more modern, visually appealing, and user-friendly experience. Focus on typography, colors, spacing, and component styling to ensure a cohesive and polished design.
Look and feel
Each slider illustrates characteristics of the customer's brand and the style your logo design should communicate.

```html
<!DOCTYPE html>
<html lang="en">
<head>
<meta charset="utf-8">
<title>FlorQuay app – UI style guide</title>
<link href="https://fonts.googleapis.com/css2?family=Figtree:wght@400;500;600;700&family=Nunito+Sans:wght@400;600;700&family=Inter:wght@400;600;700&display=swap" rel="stylesheet">
<style>
:root{
  --primary:#1B7ECC;--ink:#1C1F34;--slate:#4B4B5A;--grey:#636669;--muted:#7C848B;
  --mist:#F2F6F7;--haze:#E2E7F1;--cyan:#25C2E3;--green:#29BA85;--orange:#F77E53;
  --yellow:#FFBE0B;--pink:#FF5C75;--violet:#7859F4;--legacy-link:#0a1ed6;
}
*{box-sizing:border-box;margin:0;padding:0}
html,body{width:1200px;height:1081px;overflow:hidden;background:#fff}
body{font-family:'Figtree',sans-serif;color:var(--ink)}
.sheet{position:relative;width:1200px;height:1081px}
.title{position:absolute;left:72px;top:72px;font-size:49px;font-weight:700;letter-spacing:-.5px}
.label{position:absolute;top:154px;font-size:16px;font-weight:600;color:var(--muted)}
.swatch{position:absolute;width:48px;height:48px;border-radius:3px;font-size:10px;color:#fff;display:flex;align-items:center;justify-content:center}
.swatch.light{color:var(--slate)}
.font-sample{position:absolute;left:480px;font-size:39px;color:#000}
.section-bar{position:absolute;left:72px;top:433px;width:1056px;height:45px;background:#000;color:#fff;font-weight:700;font-size:17px;padding:12px 13px}
.screen{position:absolute;top:502px;width:234px;height:506px;overflow:hidden;background:#fff}
/* legacy */
.legacy{font-family:'Inter',sans-serif}
.legacy .status{height:29px;background:#000;color:#fff;font-size:10px;font-weight:600;padding:9px 34px;display:flex;justify-content:space-between}
.legacy .nav{height:34px;background:#F2F2F7;font-size:10px;display:flex;align-items:center;justify-content:center;position:relative}
.legacy .nav .acts{position:absolute;right:14px;font-size:13px;letter-spacing:6px}
.legacy .search{margin:3px 3px 0;height:21px;border:1px solid #c8c8cc;border-radius:3px;font-size:8px;color:#555;display:flex;align-items:center;padding:0 8px;justify-content:space-between;background:#fff}
.legacy .search small{font-size:6px;color:#9ab;text-align:center;line-height:1}
.legacy .list{position:absolute;top:92px;left:0;right:0;height:366px;overflow:hidden;background:#e9e9ee;padding:0 3px}
.legacy .item{height:48px;margin-bottom:2px;background:#F7F8FA;border:1px solid #ddd;position:relative}
.legacy .box{position:absolute;left:8px;top:6px;width:38px;height:38px;border:1px solid #556;font-size:14px;color:#889;display:flex;align-items:center;justify-content:center}
.legacy .name{position:absolute;left:52px;top:9px;font-size:9px;font-weight:700;color:var(--legacy-link);white-space:nowrap}
.legacy .tags{position:absolute;left:58px;top:32px;font-size:7.5px;font-weight:600;white-space:nowrap;display:flex;gap:10px}
.legacy .tags .q{background:#5ee06a;padding:0 2px}
.legacy .tags .p{background:#fff6cc;padding:0 2px}
.legacy .tabs{position:absolute;top:458px;left:0;right:0;height:48px;background:#fff;display:flex}
.legacy .tab{flex:1;text-align:center;font-size:6.5px;padding-top:5px}
.legacy .tab.on{color:var(--primary)}
.legacy .home{position:absolute;bottom:6px;left:75px;width:84px;height:2px;background:#999;border-radius:2px}
/* refined */
.refined{border-radius:30px;background:var(--mist)}
.refined .band{position:absolute;top:0;left:0;right:0;height:151px;background:var(--primary)}
.refined .time{position:absolute;top:11px;left:22px;color:#fff;font-size:10px;font-weight:600}
.refined .island{position:absolute;top:6px;left:78px;width:77px;height:22px;background:#000;border-radius:11px}
.refined .sys{position:absolute;top:12px;right:16px}
.refined .acts{position:absolute;top:36px;right:14px;color:#fff;font-size:15px;letter-spacing:9px}
.refined h1{position:absolute;top:59px;left:10px;color:#fff;font-size:20px;font-weight:700}
.refined .search{position:absolute;top:92px;left:10px;right:10px;height:27px;border-radius:14px;background:#1a6db0;color:#9fc5e6;font-size:10px;display:flex;align-items:center;gap:7px;padding:0 9px}
.refined .search svg:last-child{margin-left:auto}
.refined .list{position:absolute;top:129px;left:9px;right:9px;height:322px;overflow:hidden;display:flex;flex-direction:column;gap:3px}
.refined .card{flex:none;height:48px;background:#fff;border-radius:8px;position:relative}
.refined .av{position:absolute;left:9px;top:9px;width:30px;height:30px;border-radius:50%;color:#fff;font-size:8.5px;display:flex;align-items:center;justify-content:center;font-family:'Nunito Sans',sans-serif}
.refined .nm{position:absolute;left:49px;top:10px;font-size:12px;white-space:nowrap;width:132px;overflow:hidden}
.refined .sub{position:absolute;left:49px;top:28px;font-size:7px;color:var(--grey);display:flex;gap:3px;white-space:nowrap;width:130px;overflow:hidden;font-family:'Nunito Sans',sans-serif}
.refined .sub span.chip{background:var(--mist);border-radius:6px;padding:1px 4px}
.refined .sub.meta{gap:0;top:29px}
.refined .sub.meta i{font-style:normal;border-left:1px solid #c5cad2;margin-left:5px;padding-left:5px}
.refined .chev{position:absolute;right:12px;top:18px}
.refined .tabs{position:absolute;top:451px;left:0;right:0;height:55px;background:#fff;display:flex;padding:0 4px}
.refined .tab{flex:1;text-align:center;font-size:6px;color:var(--muted);padding-top:5px;position:relative}
.refined .tab svg{display:block;margin:0 auto 3px;position:relative}
.refined .tab.on{color:var(--primary)}
.refined .tab.on::before{content:"";position:absolute;top:3px;left:4px;right:4px;height:17px;border-radius:9px;background:#dbeaf8}
.refined .home{position:absolute;bottom:8px;left:77px;width:80px;height:3px;background:#000;border-radius:2px}
</style>
</head>
<body>
<div class="sheet">
  <div class="title">FlorQuay app</div>
  <div class="label" style="left:72px">Colors</div>
  <div class="label" style="left:480px">Fonts</div>

  <div class="swatch" style="left:72px;top:188px;background:var(--primary)">1B7ECC</div>
  <div class="swatch" style="left:129.6px;top:188px;background:var(--ink)">1C1F34</div>
  <div class="swatch" style="left:187.2px;top:188px;background:var(--slate)">4B4B5A</div>
  <div class="swatch" style="left:244.8px;top:188px;background:var(--grey)">636669</div>
  <div class="swatch" style="left:302.4px;top:188px;background:var(--muted)">7C848B</div>
  <div class="swatch light" style="left:72px;top:251px;background:var(--mist)">F2F6F7</div>
  <div class="swatch light" style="left:129.6px;top:251px;background:var(--haze)">E2E7F1</div>
  <div class="swatch" style="left:72px;top:313px;background:var(--cyan)">25C2E3</div>
  <div class="swatch" style="left:129.6px;top:313px;background:var(--green)">29BA85</div>
  <div class="swatch" style="left:187.2px;top:313px;background:var(--orange)">F77E53</div>
  <div class="swatch" style="left:244.8px;top:313px;background:var(--yellow)">FFBE0B</div>
  <div class="swatch" style="left:302.4px;top:313px;background:var(--pink)">FF5C75</div>
  <div class="swatch" style="left:360px;top:313px;background:var(--violet)">7859F4</div>

  <div class="font-sample" style="top:188px;font-family:'Figtree',sans-serif">Figtree</div>
  <div class="font-sample" style="top:250px;font-family:'Nunito Sans',sans-serif">Nunito Sans</div>

  <div class="section-bar">List Page</div>

  <!-- Legacy contacts -->
  <div class="screen legacy" style="left:72px">
    <div class="status"><span>3:01</span><span>···· ▰</span></div>
    <div class="nav">Contacts<span class="acts">+···</span></div>
    <div class="search"><span>⚲ Search</span><small>Advanced<br>Search</small></div>
    <div class="list">
      <div class="item"><div class="box">A</div><div class="name">Ashby, Crane</div><div class="tags"><span>Aircraft Owner</span><span>Enthusiast -e</span><span>Flight Supp</span></div></div>
      <div class="item"><div class="box">A</div><div class="name">Alder, Colin, Bram</div><div class="tags"><span>Aircraft Owner</span><span class="p">Pilot</span><span class="q">Qualified Pilot</span></div></div>
      <div class="item"><div class="box">B</div><div class="name">Barlow, Rhys</div><div class="tags"><span>Aircraft Owner</span><span class="p">Pilot</span><span class="q">Qualified Pilot</span></div></div>
      <div class="item"><div class="box">B</div><div class="name">Bennick, Arlo</div><div class="tags"><span>Aircraft Owner</span><span class="p">Pilot</span><span class="q">Qualified Pilot</span></div></div>
      <div class="item"><div class="box">C</div><div class="name">Carver, Ada, Selene</div><div class="tags"><span class="p">Pilot</span></div></div>
      <div class="item"><div class="box">C</div><div class="name">Castell Ruiz, Hugo, Yarel</div><div class="tags"><span class="p">Pilot</span></div></div>
      <div class="item"><div class="box">G</div><div class="name">Gentry, Cole</div><div class="tags"><span>Aircraft Owner</span><span class="p">Pilot</span><span class="q">Qualified Pilot</span></div></div>
      <div class="item"><div class="box">G</div><div class="name">Galen, Jonah, Avery</div></div>
    </div>
    <div class="tabs"><div class="tab on">●<br>Contact</div><div class="tab">♙<br>Pilot</div><div class="tab">✈<br>Plane</div><div class="tab">☝<br>Flt Request</div><div class="tab">···<br>More</div></div>
    <div class="home"></div>
  </div>

  <!-- Refined contacts -->
  <div class="screen refined" style="left:331px">
    <div class="band"></div>
    <div class="time">9:41</div><div class="island"></div>
    <svg class="sys" width="44" height="8" viewBox="0 0 44 8"><rect x="0" y="5" width="2" height="3" fill="#fff"/><rect x="3" y="3.5" width="2" height="4.5" fill="#fff"/><rect x="6" y="2" width="2" height="6" fill="#fff"/><rect x="9" y="0" width="2" height="8" fill="#fff"/><path d="M15 3a6 6 0 0 1 8 0l-4 5z" fill="#fff"/><rect x="28" y="1" width="14" height="6.5" rx="2" fill="#fff"/></svg>
    <div class="acts">+···</div>
    <h1>Contact</h1>
    <div class="search"><svg width="11" height="11" viewBox="0 0 12 12" fill="none" stroke="#9fc5e6" stroke-width="1.4"><circle cx="5" cy="5" r="4"/><path d="M8 8l3 3"/></svg>Search<svg width="12" height="10" viewBox="0 0 12 10" fill="none" stroke="#9fc5e6"><path d="M0 2h12M0 8h12"/><circle cx="8" cy="2" r="1.5" fill="#1a6db0"/><circle cx="4" cy="8" r="1.5" fill="#1a6db0"/></svg></div>
    <div class="list">
      <div class="card"><div class="av" style="background:var(--green)">AC</div><div class="nm">Ashby, Crane</div><div class="sub"><span class="chip">Aircraft Owner</span><span class="chip">Enthusiast</span><span class="chip">Flight</span></div><svg class="chev" width="6" height="10" viewBox="0 0 6 10"><path d="M1 1l4 4-4 4" stroke="#636669" fill="none"/></svg></div>
      <div class="card"><div class="av" style="background:var(--cyan)">ACB</div><div class="nm">Alder, Colin, Bram</div><div class="sub"><span class="chip">Aircraft Owner</span><span class="chip">Pilot</span><span class="chip">Qualified Pilot</span></div><svg class="chev" width="6" height="10" viewBox="0 0 6 10"><path d="M1 1l4 4-4 4" stroke="#636669" fill="none"/></svg></div>
      <div class="card"><div class="av" style="background:var(--pink)">BR</div><div class="nm">Barlow, Rhys</div><div class="sub"><span class="chip">Aircraft Owner</span><span class="chip">Pilot</span><span class="chip">Qualified Pilot</span></div><svg class="chev" width="6" height="10" viewBox="0 0 6 10"><path d="M1 1l4 4-4 4" stroke="#636669" fill="none"/></svg></div>
      <div class="card"><div class="av" style="background:var(--yellow)">BA</div><div class="nm">Bennick, Arlo</div><div class="sub"><span class="chip">Aircraft Owner</span><span class="chip">Pilot</span><span class="chip">Qualified Pilot</span></div><svg class="chev" width="6" height="10" viewBox="0 0 6 10"><path d="M1 1l4 4-4 4" stroke="#636669" fill="none"/></svg></div>
      <div class="card"><div class="av" style="background:var(--orange)">CAS</div><div class="nm">Carver, Ada, Selene</div><div class="sub"><span class="chip">Pilot</span></div><svg class="chev" width="6" height="10" viewBox="0 0 6 10"><path d="M1 1l4 4-4 4" stroke="#636669" fill="none"/></svg></div>
      <div class="card"><div class="av" style="background:var(--violet)">CHY</div><div class="nm">Castell Ruiz, Hugo, Yarel</div><div class="sub"><span class="chip">Pilot</span></div><svg class="chev" width="6" height="10" viewBox="0 0 6 10"><path d="M1 1l4 4-4 4" stroke="#636669" fill="none"/></svg></div>
      <div class="card"><div class="av" style="background:var(--green)">GC</div><div class="nm">Gentry, Cole</div></div>
    </div>
    <div class="tabs">
      <div class="tab on"><svg width="11" height="13" viewBox="0 0 11 13" fill="none" stroke="currentColor"><rect x="1" y="1" width="9" height="11" rx="1.5"/><circle cx="5.5" cy="5" r="1.6"/><path d="M3 9.5c1-2 4-2 5 0"/></svg>Contact</div>
      <div class="tab"><svg width="11" height="13" viewBox="0 0 11 13" fill="none" stroke="currentColor"><path d="M2 3h7l-1 2H3z"/><circle cx="5.5" cy="7" r="2"/><path d="M1.5 12.5c1-3 7-3 8 0"/></svg>Pilot</div>
      <div class="tab"><svg width="13" height="13" viewBox="0 0 13 13" fill="none" stroke="currentColor"><path d="M6.5 1v11M1 7l5.5-2 5.5 2M4.5 12h4"/></svg>Plane</div>
      <div class="tab"><svg width="11" height="13" viewBox="0 0 11 13" fill="none" stroke="currentColor"><path d="M4 7V2a1 1 0 0 1 2 0v4l3 1v3l-2 2H4L2 9z"/></svg>Flt Request</div>
      <div class="tab"><svg width="12" height="13" viewBox="0 0 12 13" fill="none" stroke="currentColor"><path d="M1 3h10M1 6.5h10M1 10h10"/></svg>More</div>
    </div>
    <div class="home"></div>
  </div>

  <!-- Legacy pilots -->
  <div class="screen legacy" style="left:636px">
    <div class="status"><span>3:01</span><span>···· ▰</span></div>
    <div class="nav">Pilots<span class="acts">+···</span></div>
    <div class="search"><span>⚲ Search</span><small>Advanced<br>Search</small></div>
    <div class="list" style="padding-top:0">
      <div class="item" style="height:18px;margin-top:-8px"><div class="box" style="top:-30px"></div></div>
      <div class="item"><div class="box">A</div><div class="name">Alder, Colin, Bram, 5207418, 7/14/24</div></div>
      <div class="item"><div class="box">B</div><div class="name">Barlow, Rhys, 6031928, 1/19/25</div></div>
      <div class="item"><div class="box">B</div><div class="name">Bennick, Arlo, 8145306, 11/8/24, 16</div></div>
      <div class="item"><div class="box">C</div><div class="name">Carver, Ada, Selene, 3972641, 4/22/25,</div></div>
      <div class="item"><div class="box">C</div><div class="name">Castell Ruiz, Hugo, Yarel,</div></div>
      <div class="item"><div class="box">G</div><div class="name">Gentry, Cole, 7516042, 12/5/25,</div></div>
      <div class="item"><div class="box">G</div><div class="name">Galen, Jonah, Avery, 9384257, 5/17/23</div></div>
    </div>
    <div class="tabs"><div class="tab">●<br>Contact</div><div class="tab on">♙<br>Pilot</div><div class="tab">✈<br>Plane</div><div class="tab">☝<br>Flt Request</div><div class="tab">···<br>More</div></div>
    <div class="home"></div>
  </div>

  <!-- Refined pilots -->
  <div class="screen refined" style="left:895px">
    <div class="band"></div>
    <div class="time">9:41</div><div class="island"></div>
    <svg class="sys" width="44" height="8" viewBox="0 0 44 8"><rect x="0" y="5" width="2" height="3" fill="#fff"/><rect x="3" y="3.5" width="2" height="4.5" fill="#fff"/><rect x="6" y="2" width="2" height="6" fill="#fff"/><rect x="9" y="0" width="2" height="8" fill="#fff"/><path d="M15 3a6 6 0 0 1 8 0l-4 5z" fill="#fff"/><rect x="28" y="1" width="14" height="6.5" rx="2" fill="#fff"/></svg>
    <div class="acts">+···</div>
    <h1>Pilot</h1>
    <div class="search"><svg width="11" height="11" viewBox="0 0 12 12" fill="none" stroke="#9fc5e6" stroke-width="1.4"><circle cx="5" cy="5" r="4"/><path d="M8 8l3 3"/></svg>Search<svg width="12" height="10" viewBox="0 0 12 10" fill="none" stroke="#9fc5e6"><path d="M0 2h12M0 8h12"/><circle cx="8" cy="2" r="1.5" fill="#1a6db0"/><circle cx="4" cy="8" r="1.5" fill="#1a6db0"/></svg></div>
    <div class="list">
      <div class="card"><div class="av" style="background:var(--cyan)">ACB</div><div class="nm">Alder, Colin, Bram</div><div class="sub meta">5207418<i>7/14/24</i></div><svg class="chev" width="6" height="10" viewBox="0 0 6 10"><path d="M1 1l4 4-4 4" stroke="#636669" fill="none"/></svg></div>
      <div class="card"><div class="av" style="background:var(--pink)">BR</div><div class="nm">Barlow, Rhys</div><div class="sub meta">6031928<i>1/19/25</i></div><svg class="chev" width="6" height="10" viewBox="0 0 6 10"><path d="M1 1l4 4-4 4" stroke="#636669" fill="none"/></svg></div>
      <div class="card"><div class="av" style="background:var(--yellow)">BA</div><div class="nm">Bennick, Arlo</div><div class="sub meta">8145306<i>11/8/24</i></div><svg class="chev" width="6" height="10" viewBox="0 0 6 10"><path d="M1 1l4 4-4 4" stroke="#636669" fill="none"/></svg></div>
      <div class="card"><div class="av" style="background:var(--orange)">CAS</div><div class="nm">Carver, Ada, Selene</div><div class="sub meta">3972641<i>4/22/25</i></div><svg class="chev" width="6" height="10" viewBox="0 0 6 10"><path d="M1 1l4 4-4 4" stroke="#636669" fill="none"/></svg></div>
      <div class="card"><div class="av" style="background:var(--violet)">CHY</div><div class="nm" style="top:17px">Castell Ruiz, Hugo, Yarel</div><svg class="chev" width="6" height="10" viewBox="0 0 6 10"><path d="M1 1l4 4-4 4" stroke="#636669" fill="none"/></svg></div>
      <div class="card"><div class="av" style="background:var(--green)">GC</div><div class="nm">Gentry, Cole</div><div class="sub meta">7516042<i>12/5/23</i></div><svg class="chev" width="6" height="10" viewBox="0 0 6 10"><path d="M1 1l4 4-4 4" stroke="#636669" fill="none"/></svg></div>
      <div class="card"><div class="av" style="background:var(--cyan)">GJA</div></div>
    </div>
    <div class="tabs">
      <div class="tab"><svg width="11" height="13" viewBox="0 0 11 13" fill="none" stroke="currentColor"><rect x="1" y="1" width="9" height="11" rx="1.5"/><circle cx="5.5" cy="5" r="1.6"/><path d="M3 9.5c1-2 4-2 5 0"/></svg>Contact</div>
      <div class="tab on"><svg width="11" height="13" viewBox="0 0 11 13" fill="none" stroke="currentColor"><path d="M2 3h7l-1 2H3z"/><circle cx="5.5" cy="7" r="2"/><path d="M1.5 12.5c1-3 7-3 8 0"/></svg>Pilot</div>
      <div class="tab"><svg width="13" height="13" viewBox="0 0 13 13" fill="none" stroke="currentColor"><path d="M6.5 1v11M1 7l5.5-2 5.5 2M4.5 12h4"/></svg>Plane</div>
      <div class="tab"><svg width="11" height="13" viewBox="0 0 11 13" fill="none" stroke="currentColor"><path d="M4 7V2a1 1 0 0 1 2 0v4l3 1v3l-2 2H4L2 9z"/></svg>Flt Request</div>
      <div class="tab"><svg width="12" height="13" viewBox="0 0 12 13" fill="none" stroke="currentColor"><path d="M1 3h10M1 6.5h10M1 10h10"/></svg>More</div>
    </div>
    <div class="home"></div>
  </div>
</div>
</body>
</html>
```